Website re-design wedding music business

I need my wordpress wedding music website redesigned. I'm a wedding pianist and also provide duo/trio entertainment with other musicians and looking for an overhaul of my wordpress site.

Website: tollykessing.com.au

Target Market(s)

brides; engaged couples

Industry/Entity Type

Wedding

Number of Pages Required

5+ page

Colors

Designer to choose colors to be used in the design.

Requirements
Must have
• I'm looking to overhaul my website which is looking rather tired after 4 years. It is functional but not inviting to visitors. Initially my website started out as a solo piano player providing music for wedding. It is gradually growing now where brides can book
• 1) Solo Piano
• 2) Duo (any combination of Piano / Cello / Vocalist / Violin)
• 3) Trio (any combination of Piano/ Cello /Vocalist / Violin)
• in future it may increase to 4 / 5 /6 piece bands so that needs to be taken into account for the future growth where I'll recruit other musicians.
• Some other functionality I'd like to see
• - Visitors want a calendar to know availability of musicians
• - Automatically providing enquiry price & discount (if applicable)
• - Automating the booking form process (manual) - There's a PDF form I send to the customer after we go back/forth on email on songs/price etc but if more of it could be automated online that would be great. If move to online it would be good to be able to override the set prices with a custom price and also providing a payment gateway
• More Flexibility on pricing - customer selects type of artists they want and it calculates a price based on who they have chosen whether it is a ceremony or canapes or reception (or combination of any). Extra transport fee is added if >50km out of Melbourne.
• How would you re-design this website. Imagine you are a bride/groom looking to book wedding music services. I would love to see some concepts .
• Please indicate any other fees required for your submission and level of support post this competition. I would like this to be an on-going relationship.
Nice to have
• I'd preferably like the website to be in wordpress as I've been familiar with it over time and can do basic updates in the back end. Happy for other suggestions if you can convince me I should move away from wordpress.

```html
<!DOCTYPE html>
<html lang="en">
<head>
<meta charset="utf-8">
<title>Tolly Kessing – Wedding Pianist</title>
<link rel="stylesheet" href="https://fonts.googleapis.com/css2?family=Lato:wght@300;400;700&family=Open+Sans:ital,wght@0,400;0,600;1,400&display=swap">
<style>
:root{
  --ink:#1b1b1b;
  --text:#444;
  --muted:#9a9a9a;
  --line:#d9d9d9;
  --white:#fff;
  --hero-dark:#141414;
  --hero-mid:#5a5a5a;
  --orange:#f25a1a;
  --star:#f2a31a;
  --social:#2f6fb5;
  --footer-band:#f2f2f2;
  --footer-bar:#161616;
}
*{box-sizing:border-box;margin:0;padding:0}
html,body{width:1200px;height:2200px;overflow:hidden;background:var(--white)}
body{position:relative;font-family:"Lato",sans-serif;color:var(--ink)}
.abs{position:absolute}

/* header */
.brand{left:48px;top:30px;display:flex;align-items:center;gap:14px}
.brand-dot{width:56px;height:56px;border-radius:50%;background:var(--ink)}
.brand-name{font-size:27px;font-weight:400;letter-spacing:.5px;color:var(--ink)}
.head-social{top:44px;left:1070px;display:flex;gap:10px}
.head-social span{width:22px;height:22px;border:1.5px solid var(--social);display:block}
.head-social span:last-child{border-color:#d9822b}
.main-nav{top:116px;left:72px;width:1072px;display:flex;justify-content:space-between;font-size:13.5px;letter-spacing:.3px;color:#555}
.main-nav a{color:inherit;text-decoration:none;padding-bottom:10px}
.main-nav a.active{color:var(--ink);font-weight:700;border-bottom:2px solid var(--ink)}
.nav-rule{top:146px;left:0;width:1200px;height:4px;background:linear-gradient(#ddd,#f5f5f5)}

/* hero */
.hero{top:151px;left:0;width:1200px;height:580px;background:linear-gradient(100deg,var(--hero-dark) 0%,#2a2a2a 40%,var(--hero-mid) 70%,#cfcfcf 100%)}
.hero-copy{left:132px;top:318px;color:var(--white)}
.hero-title{font-size:45px;font-weight:300;letter-spacing:1px}
.hero-title b{font-weight:700}
.hero-sub{font-size:21px;font-weight:400;letter-spacing:1.5px;margin-top:2px}
.hero-text{font-family:"Open Sans",sans-serif;font-size:13px;line-height:17px;color:#bbb;width:385px;margin-top:12px}
.btn{display:inline-flex;align-items:center;justify-content:center;border:1.5px solid currentColor;font-size:14px;letter-spacing:1.5px;text-transform:uppercase}
.hero-btn{left:132px;top:508px;width:154px;height:39px;color:var(--white)}
.dots{top:675px;left:568px;display:flex;gap:12px}
.dots span{width:13px;height:13px;border-radius:50%;border:2px solid var(--white)}
.dots span:first-child{background:var(--white)}

/* feature tiles */
.tile{top:741px;height:239px;color:var(--white);text-align:center}
.tile-cd{left:0;width:390px;background:linear-gradient(120deg,#3a3a3a,#6d6d6d 50%,#2b2b2b)}
.tile-piano{left:403px;width:394px;background:linear-gradient(100deg,#3c3a36,#77736c 55%,#2e2c29)}
.tile-gallery{left:807px;width:393px;background:linear-gradient(110deg,#2d2d2d,#5f5c58 50%,#2a2a2a)}
.tile-title{position:absolute;left:0;right:0;font-weight:400;letter-spacing:1px}
.tile-cd .tile-title{top:54px;font-size:46px;left:-75px}
.tile-piano .tile-title{top:48px;font-size:32px;font-weight:300;line-height:38px}
.tile-piano .tile-title b{font-weight:400;letter-spacing:2px}
.tile-gallery .tile-title{top:54px;font-size:46px;font-weight:300;letter-spacing:3px}
.tile .btn{position:absolute;height:44px;width:144px;font-size:14px}
.tile-cd .btn{left:120px;top:142px}
.tile-piano .btn{left:122px;top:154px}
.tile-gallery .btn{left:123px;top:136px}

/* about */
.about-back{left:78px;top:1056px;width:287px;height:235px;background:#9e9e9e}
.about-photo{left:103px;top:1078px;width:287px;height:235px;background:linear-gradient(135deg,#7b8a5e,#4e5a3a 45%,#2b2b2b 70%,#d8d8d8)}
.about-copy{left:484px;top:1100px;width:620px}
.about-copy h2{font-size:33px;font-weight:300;letter-spacing:.5px}
.about-copy h2 b{font-weight:400}
.about-copy p{font-family:"Open Sans",sans-serif;font-size:15px;line-height:28px;color:var(--muted);margin-top:14px}
.about-btn{left:484px;top:1276px;width:134px;height:37px;font-size:12px;letter-spacing:.5px;color:var(--ink)}
.divider{top:1385px;left:88px;width:1009px;height:1px;background:var(--line)}

/* columns */
.col-title{top:1464px;font-size:31px;font-weight:300}
.col-title b{font-weight:400}
.events{left:91px;top:1544px;width:280px}
.event{display:flex;gap:14px;position:absolute;left:0}
.date{width:47px;height:47px;border:2px solid var(--ink);text-align:center;padding-top:3px;flex:none}
.date b{display:block;font-family:"Open Sans",sans-serif;font-weight:400;font-size:18px;line-height:20px}
.date i{display:block;font-style:normal;font-size:9px;font-family:"Open Sans",sans-serif}
.event-name{font-family:"Open Sans",sans-serif;font-size:13px;line-height:17px;color:var(--ink);width:210px}
.event-time{font-family:"Open Sans",sans-serif;font-size:13px;color:#aaa;margin-top:2px}
.events-btn{left:91px;top:1916px;width:135px;height:38px;font-size:12px;letter-spacing:.5px;color:var(--ink)}

.player{left:445px;top:1533px;width:242px;height:418px;font-family:"Open Sans",sans-serif}
.play{position:absolute;left:3px;top:4px;width:40px;height:40px;border-radius:50%;background:var(--orange)}
.player-head{position:absolute;left:50px;top:12px;font-size:12px;color:#666}
.player-src{position:absolute;left:145px;top:12px;font-size:8px;color:#ccc;letter-spacing:.5px}
.wave{position:absolute;left:5px;top:42px}
.plays{position:absolute;left:190px;top:130px;font-size:9px;color:#ccc}
.tracks{position:absolute;left:0;top:152px;width:242px;list-style:none}
.tracks li{height:29px;border-top:1px solid #eee;display:flex;align-items:center;font-size:10px;color:#333;letter-spacing:.3px}
.tracks li .art{width:14px;height:14px;background:#3a3a3a;margin:0 8px 0 8px}
.tracks li .nm{width:135px;white-space:nowrap;overflow:hidden}
.tracks li .ct{color:#aaa;font-size:10px}
.thumbs{position:absolute;left:8px;top:302px}
.thumbs span{display:block;width:17px;height:17px;background:#c97b6a;margin-bottom:19px}
.player-foot{position:absolute;left:0;top:370px;width:242px;height:48px;background:#f3f3f3;border-top:1px solid #ddd}
.player-foot .art{position:absolute;left:8px;top:7px;width:34px;height:26px;background:#2d2d2d}
.player-foot .t1{position:absolute;left:52px;top:8px;font-size:9px;color:#555}
.player-foot .t2{position:absolute;left:52px;top:21px;font-size:9.5px;font-weight:600;color:#222}
.player-foot .t3{position:absolute;left:2px;top:36px;font-size:8px;color:#666}

.testimonial{left:758px;top:1540px;width:380px;font-family:"Open Sans",sans-serif}
.avatar{position:absolute;left:0;top:0;width:56px;height:56px;border-radius:50%;background:linear-gradient(#c98a6a,#8a4a36)}
.t-name{position:absolute;left:74px;top:8px;font-size:16px;color:var(--ink)}
.t-name small{font-size:12px;color:#bbb;margin-left:10px}
.stars{position:absolute;left:74px;top:32px;display:flex;gap:2px;align-items:center}
.stars em{font-style:normal;font-size:12px;color:var(--star);margin-left:8px}
.t-quote{position:absolute;left:9px;top:66px;width:360px;font-style:italic;font-size:12.5px;line-height:17px;color:var(--ink)}
.t-body{position:absolute;left:9px;top:116px;width:362px;font-size:13px;line-height:20.6px;color:#999}
.arrows{left:771px;top:1911px;display:flex;gap:10px}
.arrows span{width:28px;height:28px;border:1.5px solid var(--ink);display:flex;align-items:center;justify-content:center}

/* footer */
.foot-band{top:2071px;left:0;width:1200px;height:74px;background:var(--footer-band)}
.foot-nav{top:2100px;font-size:13.5px;color:var(--ink);letter-spacing:.3px}
.foot-social{top:2094px;left:922px;display:flex;gap:8px}
.foot-social span{width:28px;height:28px;border-radius:50%;border:1.5px solid var(--social)}
.foot-social span:nth-child(4),.foot-social span:nth-child(5){border-color:#c0392b}
.foot-social span:nth-child(6){border-color:#d9822b}
.foot-bar{top:2145px;left:0;width:1200px;height:55px;background:var(--footer-bar);color:#ddd;font-size:17px;font-weight:300;padding:20px 0 0 88px}
</style>
</head>
<body>

<header>
  <div class="abs brand"><span class="brand-dot"></span><span class="brand-name">TOLLYKESSING</span></div>
  <div class="abs head-social" aria-label="Social links"><span></span><span></span><span></span></div>
  <nav class="abs main-nav">
    <a class="active">HOME</a><a>ABOUT</a><a>EVENTS</a><a>MUSIC</a><a>VIDEO</a><a>REPERTOIRE</a><a>PRICES</a><a>GALLERY</a><a>TESTIMONIALS</a><a>BUY CD</a><a>FAQs</a><a>CONTACT</a>
  </nav>
  <div class="abs nav-rule"></div>
</header>

<section class="abs hero" role="img" aria-label="Black and white close-up photo of grand piano keys"></section>
<div class="abs hero-copy">
  <h1 class="hero-title">TOLLY <b>KESSING</b></h1>
  <div class="hero-sub">Wedding Pianist | Event Pianist</div>
  <p class="hero-text">Tolly Kessing is Melbourne's premier award wedding &amp; event pianist specialising in playing beautiful back-ground music for weddings, special occasions &amp; corpo-rate events.</p>
</div>
<a class="abs btn hero-btn">Book Now</a>
<div class="abs dots"><span></span><span></span><span></span></div>

<section class="abs tile tile-cd" role="img" aria-label="Photo of the piano CD discs and roses">
  <div class="tile-title">BUY CD</div>
  <a class="btn">Buy Now</a>
</section>
<section class="abs tile tile-piano" role="img" aria-label="Photo of the pianist beside a white baby grand piano">
  <div class="tile-title">Hire Baby<br><b>GRAND PIANO</b></div>
  <a class="btn">Hire Now</a>
</section>
<section class="abs tile tile-gallery" role="img" aria-label="Collage of wedding performance photos">
  <div class="tile-title">GALLERY</div>
  <a class="btn">View Now</a>
</section>

<div class="abs about-back"></div>
<div class="abs about-photo" role="img" aria-label="Photo of the pianist at a white grand piano outdoors under trees"></div>
<div class="abs about-copy">
  <h2>ABOUT <b>TOLLY</b></h2>
  <p>Tolly Kessing is a Melbourne professional pianist with over 5 years experience within the wedding industry and has played piano for more than 30 years</p>
</div>
<a class="abs btn about-btn">Read More</a>
<div class="abs divider"></div>

<h3 class="abs col-title" style="left:88px">Upcoming <b>Events</b></h3>
<h3 class="abs col-title" style="left:445px">Tolly’s <b>Music</b></h3>
<h3 class="abs col-title" style="left:758px">Tolly’s <b>Testimonials</b></h3>

<div class="abs events">
  <div class="event" style="top:0"><div class="date"><b>30</b><i>JUL</i></div><div><div class="event-name">Private event – Bayhaven (tbc)</div><div class="event-time">2:00 pm - 3:00 pm</div></div></div>
  <div class="event" style="top:58px"><div class="date"><b>17</b><i>AUG</i></div><div><div class="event-name">Wedding Ceremony &amp; Canapes – Larchmere Estate, Glenvale</div><div class="event-time">3:30 pm - 6:00 pm</div></div></div>
  <div class="event" style="top:127px"><div class="date"><b>20</b><i>AUG</i></div><div><div class="event-name">Private event – Bayhaven (tbc)</div><div class="event-time">2:00 pm - 3:00 pm</div></div></div>
  <div class="event" style="top:196px"><div class="date"><b>25</b><i>AUG</i></div><div><div class="event-name">Corporate event Harbourline Hotel</div><div class="event-time">7:30 pm - 9:30 pm</div></div></div>
  <div class="event" style="top:265px"><div class="date"><b>02</b><i>SEP</i></div><div><div class="event-name">wedding ceremony/canapes (piano/female vocalist)</div><div class="event-time">8:00 am - 5:00 pm</div></div></div>
</div>
<a class="abs btn events-btn">Read More</a>

<div class="abs player">
  <span class="play"><svg width="40" height="40" viewBox="0 0 40 40"><path d="M16 12 L28 20 L16 28 Z" fill="#fff"/></svg></span>
  <div class="player-head">LANTERN ROAD - ...</div>
  <div class="player-src">AUDIOWELL</div>
  <svg class="wave" width="232" height="80" viewBox="0 0 232 80">
    <g fill="#9a9a9a">
      <rect x="0" y="38" width="3" height="26"/><rect x="5" y="32" width="3" height="32"/><rect x="10" y="36" width="3" height="28"/><rect x="15" y="30" width="3" height="34"/><rect x="20" y="34" width="3" height="30"/><rect x="25" y="28" width="3" height="36"/><rect x="30" y="33" width="3" height="31"/><rect x="35" y="30" width="3" height="34"/><rect x="40" y="35" width="3" height="29"/><rect x="45" y="29" width="3" height="35"/><rect x="50" y="32" width="3" height="32"/><rect x="55" y="36" width="3" height="28"/><rect x="60" y="31" width="3" height="33"/><rect x="65" y="34" width="3" height="30"/><rect x="70" y="28" width="3" height="36"/><rect x="75" y="33" width="3" height="31"/><rect x="80" y="30" width="3" height="34"/><rect x="85" y="35" width="3" height="29"/><rect x="90" y="31" width="3" height="33"/><rect x="95" y="34" width="3" height="30"/><rect x="100" y="29" width="3" height="35"/><rect x="105" y="33" width="3" height="31"/><rect x="110" y="30" width="3" height="34"/><rect x="115" y="36" width="3" height="28"/><rect x="120" y="31" width="3" height="33"/><rect x="125" y="28" width="3" height="36"/><rect x="130" y="34" width="3" height="30"/><rect x="135" y="30" width="3" height="34"/><rect x="140" y="33" width="3" height="31"/><rect x="145" y="29" width="3" height="35"/><rect x="150" y="35" width="3" height="29"/><rect x="155" y="31" width="3" height="33"/><rect x="160" y="34" width="3" height="30"/><rect x="165" y="28" width="3" height="36"/><rect x="170" y="32" width="3" height="32"/><rect x="175" y="36" width="3" height="28"/><rect x="180" y="30" width="3" height="34"/><rect x="185" y="33" width="3" height="31"/><rect x="190" y="31" width="3" height="33"/><rect x="195" y="35" width="3" height="29"/><rect x="200" y="32" width="3" height="32"/><rect x="205" y="36" width="3" height="28"/>
    </g>
    <rect x="0" y="64" width="210" height="6" fill="#d8d8d8"/>
    <rect x="206" y="44" width="24" height="13" fill="#333"/>
    <text x="209" y="54" font-size="9" fill="#fff" font-family="Open Sans, sans-serif">3:08</text>
  </svg>
  <div class="plays">▶ 139K</div>
  <ul class="tracks">
    <li><span class="art"></span><span class="nm">LANTERN ROAD - MORNING SU…</span><span class="ct">▶ 139K</span></li>
    <li><span class="art"></span><span class="nm">ADA VELL - THE QUIET…</span><span class="ct">▶ 55.1K</span></li>
    <li><span class="art"></span><span class="nm">ROWAN PIKE - ALWAYS YO…</span><span class="ct">▶ 154K</span></li>
    <li><span class="art"></span><span class="nm">HARBOUR LIGHTS</span><span class="ct">▶ 22.2K</span></li>
    <li><span class="art"></span><span class="nm">GLASSHOUSE - SKYWARD</span><span class="ct">▶ 49.6K</span></li>
  </ul>
  <div class="thumbs"><span></span><span></span></div>
  <div class="player-foot">
    <span class="art"></span>
    <span class="t1">Tolly Kessing Piano</span>
    <span class="t2">Wedding Piano Background</span>
    <span class="t3">Cookie policy</span>
  </div>
</div>

<div class="abs testimonial">
  <div class="avatar" role="img" aria-label="Reviewer portrait"></div>
  <div class="t-name">Maren <small>25th Sept, 2017</small></div>
  <div class="stars">
    <svg width="94" height="14" viewBox="0 0 94 14" fill="#f2a31a"><path id="st" d="M7 0l2 4.6 5 .4-3.8 3.3 1.2 4.9L7 10.6 2.6 13.2l1.2-4.9L0 5l5-.4z"/><use href="#st" x="19"/><use href="#st" x="38"/><use href="#st" x="57"/><use href="#st" x="76"/></svg>
    <em>(5/ 5)</em>
  </div>
  <p class="t-quote">Would definitely recommend him for other weddings and events.</p>
  <p class="t-body">After our pianist cancelled on us a month before the wedding, Tolly truly came through for us and saved the day. He was completely professional and considerate. Tolly listened to what we wanted and was faithful to our requests. In saying that, he was also able to improvise when need be so that the event ran smoothly. A wonderfully gifted musi-cian and generally a pleasant person to work with. We received an overwhelming amount of feedback from our guests testifying to what a brilliant job Tolly did.</p>
</div>
<div class="abs arrows">
  <span><svg width="10" height="12" viewBox="0 0 10 12"><path d="M7 1 L2 6 L7 11" stroke="#1b1b1b" stroke-width="1.6" fill="none"/></svg></span>
  <span><svg width="10" height="12" viewBox="0 0 10 12"><path d="M3 1 L8 6 L3 11" stroke="#1b1b1b" stroke-width="1.6" fill="none"/></svg></span>
</div>

<footer>
  <div class="abs foot-band"></div>
  <a class="abs foot-nav" style="left:73px">HOME</a>
  <a class="abs foot-nav" style="left:183px">ABOUT</a>
  <a class="abs foot-nav" style="left:293px">SUPPLIERS</a>
  <a class="abs foot-nav" style="left:422px">INSTAGRAM</a>
  <a class="abs foot-nav" style="left:559px">BOOK NOW</a>
  <a class="abs foot-nav" style="left:695px">CONTACT</a>
  <div class="abs foot-social" aria-label="Social links"><span></span><span></span><span></span><span></span><span></span><span></span></div>
  <div class="abs foot-bar">© 2017 Copyright Tolly Kessing</div>
</footer>

</body>
</html>
```